Business Card Design

We sell fish products to corporate food companies who then turn these products into final food products for consumers

Industry/Entity Type

Business

Contact Information for Business Card

I need a corporate business card template for a fish products business. We would like it be professional for use in dealing with multi national companies. This company business card template will be used by multiple employees so the following fields must be open to edit (Name, Phone Number and Email address)

```html
<!DOCTYPE html>
<html lang="en">
<head>
<meta charset="utf-8">
<title>Tidemark Seafoods – Business Card</title>
<link href="https://fonts.googleapis.com/css2?family=Tinos:wght@400;700&display=swap" rel="stylesheet">
<style>
  :root {
    --canvas-bg: #e9e9e7;
    --card-white: #fbfbfb;
    --brand-blue: #1f64b0;
    --ink: #151515;
    --panel-light: #eaf6fb;
    --panel-sky: #bfe6f2;
    --panel-aqua: #9fdcd2;
    --divider-green: #8fd6b3;
  }
  * { margin: 0; padding: 0; box-sizing: border-box; }
  html, body {
    width: 1200px; height: 892px; overflow: hidden;
    background: var(--canvas-bg);
  }
  .canvas {
    position: relative; width: 1200px; height: 892px;
    display: flex; align-items: center; justify-content: center;
  }
  .business-card {
    position: relative; width: 1000px; height: 571px;
    background: var(--card-white);
    box-shadow: 0 10px 30px rgba(0,0,0,0.18);
    overflow: hidden;
    font-family: "Tinos", "Times New Roman", serif;
  }
  .contact-panel-shape { position: absolute; inset: 0; }
  .brand-lockup {
    position: absolute; left: 60px; top: 228px; width: 440px;
    display: flex; align-items: center; gap: 18px;
  }
  .brand-dot {
    width: 64px; height: 64px; border-radius: 50%;
    background: var(--brand-blue); flex: none;
  }
  .brand-name {
    color: var(--brand-blue); font-weight: 400;
    font-size: 46px; line-height: 1; letter-spacing: 0.5px;
  }
  .contact-block {
    position: absolute; left: 560px; right: 40px; top: 150px;
    text-align: center; color: var(--ink);
  }
  .employee-name {
    color: var(--brand-blue); font-weight: 700;
    font-size: 42px; line-height: 1.1;
  }
  .employee-title { font-size: 18px; margin-top: 6px; }
  .contact-line { font-size: 26px; line-height: 1.35; }
  .contact-lines { margin-top: 44px; }
</style>
</head>
<body>
<main class="canvas">
  <section class="business-card">
    <svg class="contact-panel-shape" width="1000" height="571" viewBox="0 0 1000 571" aria-hidden="true">
      <defs>
        <linearGradient id="panelGradient" x1="0" y1="1" x2="1" y2="0">
          <stop offset="0" stop-color="var(--panel-light)" style="stop-color:#eaf6fb"/>
          <stop offset="0.55" stop-color="#bfe6f2"/>
          <stop offset="1" stop-color="#9fdcd2"/>
        </linearGradient>
      </defs>
      <polygon points="570,0 1000,0 1000,571 538,571" fill="url(#panelGradient)"/>
      <line x1="570" y1="0" x2="538" y2="571" stroke="#8fd6b3" stroke-width="2.5"/>
    </svg>

    <div class="brand-lockup">
      <span class="brand-dot"></span>
      <span class="brand-name">Tidemark Seafoods</span>
    </div>

    <div class="contact-block">
      <p class="employee-name">Employee name</p>
      <p class="employee-title">Managing Director</p>
      <div class="contact-lines">
        <p class="contact-line">455-5012 7788</p>
        <p class="contact-line">info@tidemarkseafoods.com</p>
      </div>
    </div>
  </section>
</main>
</body>
</html>
```